Property Management Services - Capabilities Overview

We need a letter-sized brochure, preferably with a cover page, 2 pages of content, and back page. We are a multi-family property management firm, Indianapolis HQ, and we need this overview as an initial piece of collateral for investors who own Multifamily properties and are a looking for professional management services. We would like to include more photos, visuals, graphs, etc. than long-winded paragraphs. Our colors are orange, dark blue, and dark gray. We are fine with stock photos of apartment communities for some of the content. Will also upload sample brochures from competitors as well as current portfolio photos in the upload section. Feel free to use as much or as little as appropriate.

Target Market(s)

Real Estate Investors, Real Estate Brokers, Multifamily Investment Advisors

Industry/Entity Type

Property Management

Colors
0655a3
333333
f78f20

Requirements
Must have
• Visual appeal, photos, graphics, company colors (see attached Sample Colors for the appropriate shades of orange and blue), cover page with full image
Nice to have
• Sample brochures included in the upload section should be a great starting point. Placeholders for key facts, maps, team member photos, etc. would be great.
Should not have
• too much content, too much space for paragraphs and language

```html
<!DOCTYPE html>
<html lang="en">
<head>
<meta charset="utf-8">
<title>Harlow Asset Management – Capabilities Overview</title>
<link href="https://fonts.googleapis.com/css2?family=Source+Sans+3:ital,wght@0,300;0,400;0,600;1,400&display=swap" rel="stylesheet">
<style>
  :root{
    --orange:#f37a21;
    --orange-deep:#ea6f16;
    --navy:#1d2552;
    --ink:#333333;
    --grey-band:#ececec;
    --stage:#ffffff;
    --photo-light:#b9b9b9;
    --photo-dark:#5d5d5d;
  }
  *{box-sizing:border-box;margin:0;padding:0}
  html,body{width:902px;height:1200px;overflow:hidden;background:var(--stage)}
  body{position:relative;font-family:"Source Sans 3",Arial,sans-serif;color:var(--ink)}
  .spread{position:absolute;left:58px;width:801px;height:517px;background:#fff;overflow:hidden;box-shadow:0 0 0 1px #e2e2e2}
  .spread--outer{top:53px}
  .spread--inner{top:614px}
  .page{position:absolute;top:0;width:400.5px;height:517px;overflow:hidden}
  .page--left{left:0}
  .page--right{left:400.5px}
  .photo{position:absolute;background:linear-gradient(180deg,var(--photo-light),var(--photo-dark))}
  .abs{position:absolute}

  /* brand name */
  .brand{position:absolute;color:var(--orange);font-weight:400;text-align:center;line-height:1}
  .brand__mark{display:block;margin:0 auto;background:var(--orange)}
  .brand__name{display:block;letter-spacing:.04em}
  .brand__sub{display:block;letter-spacing:.32em}

  /* testimonials */
  .testimonials{left:20px;top:161px;width:170px;height:201px;background:var(--orange);color:#fff;padding:14px 5px 0 6px}
  .testimonials h3{font-weight:400;font-size:10.5px;margin-bottom:10px}
  .testimonials blockquote{font-style:italic;font-size:6.6px;line-height:1.4;text-align:justify}
  .testimonials cite{display:block;font-style:normal;font-size:6.6px;line-height:1.35;margin:3px 0 10px}

  .contact{left:19px;top:448px;list-style:none;font-size:7.4px;color:var(--ink)}
  .contact li{display:flex;align-items:flex-start;gap:7px;margin-bottom:5px;line-height:1.3}
  .contact svg{flex:none;width:8px;height:8px;margin-top:1px}

  .masthead{left:0;top:0;width:400.5px;height:102px;background:var(--grey-band)}
  .address{left:266px;top:53px;font-size:7.2px;line-height:1.72}

  .hero-band{left:0;top:318px;width:400.5px;height:135px;background:rgba(243,122,33,.88);color:#fff;padding:44px 0 0 30px}
  .hero-band h2{font-weight:400;font-size:13.6px;letter-spacing:.02em}
  .hero-band p{font-weight:300;font-size:24px;margin-top:7px}

  /* inner spread */
  .photo-band{left:0;top:57px;width:400.5px;height:142px;background:rgba(20,20,20,.55);color:#fff;padding:62px 0 0 21px}
  .photo-band p{font-weight:300;font-size:19px;line-height:1.1}

  .section-title{font-weight:400;font-size:10.5px;color:var(--navy);letter-spacing:.01em}
  .intro{left:21px;top:295px;width:170px}
  .intro p{font-size:7px;line-height:1.4;margin-top:4px;text-align:justify}
  .intro hr{border:0;border-top:1.5px solid var(--navy);margin-top:6px}

  .mission{left:21px;top:362px;width:170px;height:134px;background:var(--orange);color:#fff;padding:5px 5px;font-size:7px;line-height:1.36;text-align:justify}
  .mission p + p{margin-top:8px}

  .services{left:212px;top:373px;width:180px}
  .services h4{font-weight:600;font-size:7px;color:var(--navy);margin-bottom:6px}
  .services ul{list-style:none}
  .services li{font-size:7px;height:13.1px;display:flex;align-items:center;gap:6px}
  .services li::before{content:"›";color:var(--orange);font-weight:600;font-size:9px;line-height:1}

  .owners{left:0;top:56px;width:400.5px;height:210px;background:var(--orange);color:#fff}
  .owners__split{position:absolute;left:0;top:144px;width:100%;height:66px;background:var(--orange-deep)}
  .owners__block{position:absolute;left:29px;width:343px}
  .owners__block h3{font-weight:400;font-size:10.5px;margin-bottom:3px}
  .owners__block p{font-size:6.9px;line-height:1.38;text-align:justify}
  .owners__block p + p{margin-top:7px}

  .team-title{left:29px;top:294px}
  .leader{position:absolute;left:29px;width:200px;height:56px}
  .leader .photo{left:0;top:0;width:56px;height:56px}
  .leader__name{position:absolute;left:59px;bottom:7px;font-size:7.2px;color:var(--navy);line-height:1.1}
  .leader__name em{display:block;font-size:5.4px;color:var(--ink)}
  .staff{position:absolute;width:48px;text-align:center}
  .staff .photo{position:relative;width:48px;height:48px;border:1px solid #ddd}
  .staff__name{font-size:3.8px;line-height:1.15;margin-top:2px;color:var(--ink)}
  .staff__name em{display:block;font-size:3.2px}
</style>
</head>
<body>

<!-- Outer spread: back cover + front cover -->
<section class="spread spread--outer">
  <div class="page page--left">
    <div class="photo" style="left:0;top:0;width:400.5px;height:211px" role="img" aria-label="Black and white photo of townhouse-style apartment buildings on a green lawn"></div>

    <div class="abs testimonials">
      <h3>CLIENT Testimonials</h3>
      <blockquote>“ Harlow Asset Management manages 3 properties for us. We work with a number of property managers in various locations around the country, and Owen is head and shoulders above the rest. I wholeheartedly recommend him.</blockquote>
      <cite>- Paul Marchetti, Buyer’s Agent at Seabright Coast Properties</cite>
      <blockquote>“ Harlow Asset Management sets the bar for others to strive for from A to Z, and I cannot say enough good things about them. Great attitude, fierce work ethic and great knowledge of the property management business and Indianapolis area markets.</blockquote>
      <cite>- Dean Corwin, Homeowner &amp; GCO-Senior Counsel at Keystone Mutual</cite>
    </div>

    <ul class="abs contact">
      <li><svg viewBox="0 0 10 10"><circle cx="5" cy="5" r="5" fill="#1d2552"/><path d="M3.4 2.6l1 1-.5.7a4 4 0 0 0 1.8 1.8l.7-.5 1 1-.7.9C5 7.3 2.7 5 2.5 3.3z" fill="#fff"/></svg>(317) 555-0188</li>
      <li><svg viewBox="0 0 10 10"><circle cx="5" cy="5" r="5" fill="#1d2552"/><circle cx="5" cy="5" r="2.6" fill="none" stroke="#fff" stroke-width=".7"/><path d="M2.4 5h5.2M5 2.4v5.2" stroke="#fff" stroke-width=".5"/></svg>harlowassetmanagement.com</li>
      <li><svg viewBox="0 0 10 10"><circle cx="5" cy="5" r="5" fill="#1d2552"/><path d="M5 2a2 2 0 0 1 2 2c0 1.5-2 3.8-2 3.8S3 5.5 3 4a2 2 0 0 1 2-2z" fill="#fff"/></svg>418 E 52nd St. Indianapolis,<br>IN 46205</li>
    </ul>

    <div class="brand" style="left:214px;top:378px;width:160px">
      <span class="brand__mark" style="width:16px;height:16px;margin-bottom:10px"></span>
      <span class="brand__name" style="font-size:44px">HARLOW</span>
      <span class="brand__name" style="font-size:15px;margin-top:6px">ASSET</span>
      <span class="brand__sub" style="font-size:8.5px;margin-top:4px">MANAGEMENT</span>
    </div>
  </div>

  <div class="page page--right">
    <div class="abs masthead"></div>
    <div class="brand" style="left:32px;top:24px;width:80px">
      <span class="brand__mark" style="width:8px;height:8px;margin-bottom:5px"></span>
      <span class="brand__name" style="font-size:22px">HARLOW</span>
      <span class="brand__name" style="font-size:8px;margin-top:3px">ASSET</span>
      <span class="brand__sub" style="font-size:4.6px;margin-top:2px">MANAGEMENT</span>
    </div>
    <p class="abs address">Harlow Asset Management<br>418 E 52nd St. Indianapolis, IN 46205<br>(317) 555-0188</p>

    <div class="photo" style="left:0;top:102px;width:400.5px;height:415px" role="img" aria-label="Black and white photo of a brick apartment building entrance with a walkway"></div>
    <div class="abs hero-band">
      <h2>HARLOW ASSET MANAGEMENT</h2>
      <p>Luxury living, affordable rent.</p>
    </div>
  </div>
</section>

<!-- Inner spread: content pages -->
<section class="spread spread--inner">
  <div class="page page--left">
    <div class="photo" style="left:0;top:0;width:400.5px;height:266px" role="img" aria-label="Black and white photo of brick apartment buildings with exterior stairs"></div>
    <div class="abs photo-band">
      <p>Experience seamless<br>property management in Indianapolis</p>
    </div>

    <div class="abs intro">
      <h3 class="section-title">PROPERTY MANAGEMENT</h3>
      <p>We are an expert property management company in Indianapolis, Indiana. Harlow Asset Management’s mission is to provide excellent service to our clients.</p>
      <hr>
    </div>

    <div class="abs mission">
      <p>Harlow’s mission is simple. Whether the client owns one investment property or one hundred plus units; they get the same great service, transparent reporting, experienced advisory services and responsive communication from our team. Harlow’s industry leading platform and most importantly; Harlow’s people allow the company to strive for and achieve its mission every day.</p>
      <p>We take pride in our team, and industry leading technology that makes the property management experience accessible, transparent, seamless and simple.</p>
    </div>

    <div class="abs services">
      <h4>Our property management services include:</h4>
      <ul>
        <li>Tenant screening from every angle</li>
        <li>Monthly and Yearly financials and tax statements</li>
        <li>24/7/365 Owner account access via our platform.</li>
        <li>Targeted and effective marketing</li>
        <li>24/7/365 emergency services</li>
        <li>90% of work orders serviced</li>
        <li>Leading industry technology</li>
        <li>Reliable, experienced and dedicated staff</li>
        <li>Local expertise and network</li>
      </ul>
    </div>
  </div>

  <div class="page page--right">
    <div class="brand" style="left:30px;top:27px;width:110px;color:#b5b5b5;text-align:left">
      <span class="brand__name" style="font-size:12px">HARLOW ASSET</span>
      <span class="brand__sub" style="font-size:5px;margin-top:2px">MANAGEMENT</span>
    </div>

    <div class="abs owners">
      <div class="owners__split"></div>
      <div class="owners__block" style="top:42px">
        <h3>FOR OWNERS</h3>
        <p>Our business is to provide our clients with management solutions that help their properties operate smoothly, increase in desirability and enhance investment value.</p>
        <p>That’s why property owners throughout the area depend on us to help achieve their goals of property performance and profitability. Whether your properties are apartments, single-family homes, duplexes or condominiums, our team and our technology at Harlow Asset Management ensures that your property is well managed.</p>
      </div>
      <div class="owners__block" style="top:158px">
        <h3>FOR RESIDENTS</h3>
        <p>We manage some of the areas most desirable rentals. Our progressive staff understands that consistently working to improve the quality of service and attention to detail are the best ways to provide comfortable communities for the people who have chosen our rentals.</p>
      </div>
    </div>

    <h3 class="abs section-title team-title">HARLOW ASSET MANAGEMENT TEAM</h3>

    <div class="leader" style="top:314px">
      <div class="photo" role="img" aria-label="Portrait photo of Owen Harlow"></div>
      <p class="leader__name">Owen Harlow<em>CEO and Managing Broker</em></p>
    </div>
    <div class="leader" style="top:376px">
      <div class="photo" role="img" aria-label="Portrait photo of Grant Ellery"></div>
      <p class="leader__name">Grant Ellery<em>Director of Maintenance</em></p>
    </div>
    <div class="leader" style="top:438px">
      <div class="photo" role="img" aria-label="Portrait photo of Nadia Voss"></div>
      <p class="leader__name">Nadia Voss<em>Director of Finance &amp; Operations</em></p>
    </div>

    <div class="staff" style="left:222px;top:370px"><div class="photo" role="img" aria-label="Portrait photo of Mark Dale"></div><p class="staff__name">Mark Dale<em>Operations Coordinator</em></p></div>
    <div class="staff" style="left:279px;top:370px"><div class="photo" role="img" aria-label="Portrait photo of Lena Ford"></div><p class="staff__name">Lena Ford<em>Property Manager</em></p></div>
    <div class="staff" style="left:336px;top:370px"><div class="photo" role="img" aria-label="Portrait photo of Alice Tran"></div><p class="staff__name">Alice Tran<em>Office Manager</em></p></div>
    <div class="staff" style="left:222px;top:436px"><div class="photo" role="img" aria-label="Portrait photo of Sam Ortiz"></div><p class="staff__name">Sam Ortiz<em>Property Manager</em></p></div>
    <div class="staff" style="left:279px;top:436px"><div class="photo" role="img" aria-label="Portrait photo of Jake Moss"></div><p class="staff__name">Jake Moss<em>Property Manager</em></p></div>
    <div class="staff" style="left:336px;top:436px"><div class="photo" role="img" aria-label="Portrait photo of Tara Lyle"></div><p class="staff__name">Tara Lyle<em>Assistant Property Manager</em></p></div>
  </div>
</section>

</body>
</html>
```